GPS Tracker Business Card Design

We need a business card for a GPS Vehicle tracking company. We sell the hardware for the vehicle and the software platform to monitor your vehicle/s. Including high asset non-powered vehicles like a trailer using our solar powered unit.
We like using dark blue to different shades of blue along with gold. We have phone apps for Android and Apple devices.

We have a platform for families wanting to track their teenage driver and children; Plus a Fleet vehicle tracking platform.

Features: unlimited number of vehicles and/or assets including snow mobiles forklifts generators trailers airport equipment

Reports for driving behavior reports and alerts dashboard fleet maintenace timeline view and replay geofence real time alerts logbook scheduling route optimization accounting integration fleet grouping closest vehicle locator On Board Diagnostics.

Benefits: Increased productivity improved fuel efficiency organizing your business improve time management simplify back end processes, reduce fleet fuel efficiency and expenses increase fleet security etc..

Please view website: Velmora.com

Industry/Entity Type

Business

Contact Information for Business Card

Harold B Pennick

```html
<!DOCTYPE html>
<html lang="en">
<head>
<meta charset="utf-8">
<title>Velmora Business Card</title>
<link rel="stylesheet" href="https://fonts.googleapis.com/css2?family=Arimo:wght@400&family=Questrial&display=swap">
<style>
  :root {
    --page: #e9e9ec;
    --white: #ffffff;
    --black: #000000;
    --ink: #111111;
    --navy: #0d1847;
    --navy-deep: #0a1540;
    --brand-blue: #1f5cb4;
    --tagline-grey: #6b6b6b;
    --tagline-dim: #5f6b8a;
    --globe-light: #c9cbe6;
    --globe-pale: #eef0fb;
    --globe-blue: #2f7fd0;
    --globe-dark: #0f3f8c;
  }
  * { margin: 0; padding: 0; box-sizing: border-box; }
  html, body {
    width: 1189px; height: 1200px; overflow: hidden;
    background: var(--page);
  }
  .canvas { position: relative; width: 1189px; height: 1200px; }
  .card {
    position: absolute; left: 135px; width: 918px; height: 524px;
    overflow: hidden;
  }
  .card-front { top: 45px; background: var(--white); }
  .card-back { top: 622px; background: var(--navy-deep); }
  .card-art { position: absolute; inset: 0; width: 918px; height: 524px; }

  .brand-name {
    position: absolute; font-family: "Questrial", sans-serif; font-weight: 400;
    font-size: 118px; line-height: 1; letter-spacing: -2px; white-space: nowrap;
  }
  .brand-tagline {
    position: absolute; font-family: "Questrial", sans-serif; font-weight: 400;
    font-size: 31px; line-height: 1; letter-spacing: 0.5px; white-space: nowrap;
  }
  .card-front .brand-name { left: 52px; top: 78px; color: var(--ink); }
  .card-front .brand-tagline { left: 78px; top: 186px; color: var(--tagline-grey); }
  .card-back .brand-name { left: 76px; top: 196px; color: var(--white); }
  .card-back .brand-tagline { left: 106px; top: 308px; color: var(--tagline-dim); }

  .holder-name {
    position: absolute; right: 78px; top: 272px; white-space: nowrap;
    font-family: "Arimo", sans-serif; font-size: 42px; line-height: 1;
    color: var(--brand-blue);
  }
  .contact-list {
    position: absolute; right: 78px; top: 334px; list-style: none;
    font-family: "Arimo", sans-serif; font-size: 27px; color: var(--white);
  }
  .contact-item {
    display: flex; justify-content: flex-end; align-items: center;
    height: 27px; margin-bottom: 15px; white-space: nowrap;
  }
  .contact-item:last-child { margin-top: 5px; }
  .contact-icon {
    width: 22px; height: 22px; margin-left: 28px; flex: none; display: block;
  }
</style>
</head>
<body>
<main class="canvas">

  <section class="card card-front">
    <svg class="card-art" viewBox="0 0 918 524">
      <defs>
        <radialGradient id="globe-soft" cx="0.7" cy="0.3" r="0.8">
          <stop offset="0" stop-color="var(--globe-pale)"/>
          <stop offset="1" stop-color="var(--globe-light)"/>
        </radialGradient>
      </defs>
      <path d="M555,0 L918,0 L918,300 L640,300 C600,230 570,120 555,0 Z" fill="url(#globe-soft)" role="img" aria-label="Illustration of a dotted world globe with glowing connection lines"/>
      <path d="M0,253 C200,345 430,300 600,250 S820,205 918,290 L918,524 L0,524 Z" fill="var(--navy)"/>
      <path d="M0,305 C210,395 440,330 620,298 S840,285 918,330 L918,524 L0,524 Z" fill="var(--black)"/>
    </svg>
    <div class="brand-name">Velmora</div>
    <div class="brand-tagline">Every Mile, Every Moment</div>
    <div class="holder-name">Harold B Pennick</div>
    <ul class="contact-list">
      <li class="contact-item"><span>555-204-7781</span>
        <svg class="contact-icon" viewBox="0 0 22 22"><rect width="22" height="22" fill="var(--brand-blue)"/><path d="M5 9 Q11 4 17 9 L15 11 L13 9 L9 9 L7 11 Z M7 12 H15 V17 H7 Z" fill="var(--navy)"/></svg></li>
      <li class="contact-item"><span>www.velmora.com</span>
        <svg class="contact-icon" viewBox="0 0 22 22"><rect width="22" height="22" fill="var(--brand-blue)"/><circle cx="11" cy="11" r="6.5" fill="none" stroke="var(--navy)" stroke-width="2"/><path d="M4.5 11 H17.5 M11 4.5 V17.5" stroke="var(--navy)" stroke-width="1.5"/></svg></li>
      <li class="contact-item"><span>hello@velmora.com</span>
        <svg class="contact-icon" viewBox="0 0 22 22"><rect width="22" height="22" fill="var(--brand-blue)"/><rect x="4" y="6" width="14" height="10" fill="none" stroke="var(--navy)" stroke-width="1.6"/><path d="M4 6 L11 12 L18 6" fill="none" stroke="var(--navy)" stroke-width="1.6"/></svg></li>
      <li class="contact-item"><span>418 Birchline Rd Marlow, TX 75001</span>
        <svg class="contact-icon" viewBox="0 0 22 22"><rect width="22" height="22" fill="var(--brand-blue)"/><path d="M11 18 C7 13 6.5 11 6.5 9.5 A4.5 4.5 0 0 1 15.5 9.5 C15.5 11 15 13 11 18 Z" fill="var(--navy)"/><circle cx="11" cy="9.5" r="1.6" fill="var(--brand-blue)"/></svg></li>
    </ul>
  </section>

  <section class="card card-back">
    <svg class="card-art" viewBox="0 0 918 524">
      <defs>
        <radialGradient id="globe-bright" cx="0.55" cy="0.4" r="0.7">
          <stop offset="0" stop-color="var(--globe-blue)"/>
          <stop offset="1" stop-color="var(--globe-dark)"/>
        </radialGradient>
      </defs>
      <path d="M918,0 L918,524 L760,524 C690,470 650,380 650,270 C650,140 740,40 860,0 Z" fill="url(#globe-bright)" role="img" aria-label="Illustration of a blue dotted world globe circled by arrows and network lines"/>
    </svg>
    <div class="brand-name">Velmora</div>
    <div class="brand-tagline">Every Mile, Every Moment</div>
  </section>

</main>
</body>
</html>
```